Business Cards

Business card design for my company.
I would like the card's background colour to be black. You can also see our web site to get an idea of our brand. https://www.tmwhomecrafting.com.au/
- Name
- Email

```html
<!DOCTYPE html>
<html lang="en">
<head>
<meta charset="utf-8">
<title>TMW Home Crafting – Business Cards</title>
<link rel="stylesheet" href="https://fonts.googleapis.com/css2?family=Open+Sans:wght@400;600;700&display=swap">
<style>
  :root {
    --backdrop: #2a2b2d;
    --card-black: #1b1b1c;
    --brand-green: #119a3b;
    --text-white: #f2f2f2;
    --rule-grey: #8a8a8a;
  }
  * { box-sizing: border-box; margin: 0; padding: 0; }
  html, body {
    width: 1200px; height: 1088px; overflow: hidden;
    background: var(--backdrop);
    font-family: "Open Sans", Arial, sans-serif;
  }
  .sheet {
    width: 1200px; height: 1088px;
    display: flex; flex-direction: column; align-items: center; justify-content: center;
    gap: 48px;
  }
  .card {
    position: relative;
    width: 780px; height: 476px;
    background: var(--card-black);
    border-bottom: 6px solid var(--brand-green);
    overflow: hidden;
    box-shadow: 0 18px 40px rgba(0,0,0,.45);
  }
  /* Front */
  .brand-mark {
    position: absolute; top: 96px; left: 0; right: 0;
    display: flex; align-items: center; justify-content: center; gap: 16px;
  }
  .brand-mark .square {
    width: 34px; height: 34px; background: var(--brand-green); flex: none;
  }
  .brand-mark .brand-name {
    font-weight: 700; font-size: 38px; letter-spacing: 3px;
    color: var(--text-white); text-transform: uppercase; white-space: nowrap;
  }
  .details {
    position: absolute; top: 228px; left: 0; right: 0;
    display: flex; justify-content: center; align-items: center; gap: 22px;
  }
  .person { text-align: right; }
  .person .name {
    font-size: 22px; font-weight: 600; color: var(--brand-green);
    text-transform: uppercase; letter-spacing: .5px; line-height: 1.2;
  }
  .person .role { font-size: 18px; color: var(--text-white); }
  .divider { width: 1px; height: 92px; background: var(--rule-grey); }
  .contacts { list-style: none; }
  .contacts li {
    display: flex; align-items: center; gap: 8px;
    font-size: 18px; color: var(--text-white); line-height: 1.5;
  }
  .contacts svg { width: 15px; height: 15px; fill: var(--brand-green); flex: none; }
  .location-tab {
    position: absolute; bottom: 0; left: 180px; width: 560px; height: 82px;
    background: var(--brand-green);
    border-radius: 44px 44px 0 0;
    display: flex; align-items: center; justify-content: center;
    font-size: 19px; color: var(--text-white);
  }
  /* Back */
  .back .brand-mark { top: 0; bottom: 0; gap: 18px; }
  .back .brand-mark .brand-name { font-size: 44px; letter-spacing: 4px; }
  .back .brand-mark .square { width: 40px; height: 40px; }
</style>
</head>
<body>
<main class="sheet">
  <section class="card front">
    <div class="brand-mark">
      <span class="square"></span>
      <span class="brand-name">TMW Home Crafting</span>
    </div>
    <div class="details">
      <div class="person">
        <p class="name">Daniel Hartley</p>
        <p class="role">Managing Director</p>
      </div>
      <span class="divider"></span>
      <ul class="contacts">
        <li><svg viewBox="0 0 16 16"><path d="M3 1h3l1.5 4-2 1.3a9 9 0 0 0 4.2 4.2L11 8.5l4 1.5v3a2 2 0 0 1-2 2A12 12 0 0 1 1 3a2 2 0 0 1 2-2z"/></svg>0400 123 456</li>
        <li><svg viewBox="0 0 16 16"><path d="M1 3h14v10H1zM2 4l6 5 6-5v-.2H2z"/></svg>info@tmwhomecrafting.com.au</li>
        <li><svg viewBox="0 0 16 16"><circle cx="8" cy="8" r="7"/></svg>www.tmwhomecrafting.com.au</li>
      </ul>
    </div>
    <div class="location-tab">Eastwood Vale, Tasmania, Australia</div>
  </section>

  <section class="card back">
    <div class="brand-mark">
      <span class="square"></span>
      <span class="brand-name">TMW Home Crafting</span>
    </div>
  </section>
</main>
</body>
</html>
```